We need visit card and a letter paper for our website. thx

We have a beauty clinic in Switzerland.
https://wolkenbachtal.ch
We need a visit card.

Requirements
Must have
• see colors on website

```html
<!DOCTYPE html>
<html lang="en">
<head>
<meta charset="utf-8">
<title>Wolkenbachtal – Letterhead</title>
<link rel="stylesheet" href="https://fonts.googleapis.com/css2?family=Open+Sans:wght@400&family=Roboto:wght@400&display=swap">
<style>
  :root {
    --backdrop: #c8c8ca;
    --paper: #f5f5f5;
    --ink: #000000;
    --rose: #c63d6d;
    --body-text: #4f4f4f;
    --contact-text: #333333;
  }
  * { margin: 0; padding: 0; box-sizing: border-box; }
  html, body { width: 1200px; height: 1108px; overflow: hidden; }
  body {
    background: var(--backdrop);
    position: relative;
    font-family: "Open Sans", Arial, sans-serif;
  }
  .sheet {
    position: absolute;
    width: 535px;
    height: 758px;
    overflow: hidden;
    box-shadow: 8px 10px 18px rgba(0,0,0,0.18);
  }
  .sheet-cover { left: 253px; top: 108px; background: var(--ink); z-index: 1; }
  .sheet-letter { left: 428px; top: 248px; background: var(--paper); z-index: 2; }

  .cover-name {
    position: absolute;
    left: 59px;
    top: 335px;
    font-size: 60px;
    line-height: 80px;
    font-weight: 400;
    color: var(--rose);
    white-space: nowrap;
    letter-spacing: -0.5px;
  }

  .letter-name {
    position: absolute;
    left: 45px;
    top: 72px;
    font-size: 23px;
    line-height: 32px;
    font-weight: 400;
    color: var(--rose);
    white-space: nowrap;
  }

  .contact-list {
    position: absolute;
    left: 349px;
    top: 54px;
    list-style: none;
    font-family: "Roboto", Arial, sans-serif;
    font-size: 10.4px;
    line-height: 13px;
    color: var(--contact-text);
    white-space: nowrap;
  }
  .contact-list li { position: relative; padding-left: 14px; margin-bottom: 1px; }
  .contact-list li.address { margin-bottom: 3px; }
  .contact-list svg { position: absolute; left: 0; top: 2px; width: 9px; height: 10px; fill: var(--rose); }

  .letter-body {
    position: absolute;
    left: 49px;
    top: 193px;
    width: 438px;
    font-size: 9.5px;
    line-height: 14.7px;
    letter-spacing: -0.12px;
    color: var(--body-text);
  }
  .letter-body p { margin-bottom: 14.6px; text-align: justify; }
  .letter-body .salutation, .letter-body .closing { text-align: left; }

  .signature-area {
    margin-top: 16px;
    width: 62px;
    height: 58px;
    background: linear-gradient(135deg, #e6e6e6, #d9d9d9);
  }

  .footer-band {
    position: absolute;
    left: 0;
    bottom: 0;
    width: 535px;
    height: 8px;
  }
</style>
</head>
<body>

  <section class="sheet sheet-cover" aria-label="Cover sheet">
    <div class="cover-name">Wolkenbachtal</div>
  </section>

  <section class="sheet sheet-letter" aria-label="Letterhead">
    <div class="letter-name">Wolkenbachtal</div>

    <ul class="contact-list">
      <li class="address">
        <svg viewBox="0 0 10 12"><path d="M5 0C2.3 0 0.5 1.9 0.5 4.3 0.5 7.4 5 12 5 12s4.5-4.6 4.5-7.7C9.5 1.9 7.7 0 5 0zm0 6a1.7 1.7 0 1 1 0-3.4A1.7 1.7 0 0 1 5 6z"/></svg>
        Talweg 14, 7310<br>Birkenau, Switzerland
      </li>
      <li>
        <svg viewBox="0 0 10 10"><path d="M1 3.5C1 2 3 1.5 5 1.5S9 2 9 3.5v1H7V3.3H3v1.2H1zM2.5 5h5l1 3.5h-7z"/></svg>
        +41 (0) 800 24 60 80
      </li>
      <li>
        <svg viewBox="0 0 10 10"><path d="M0.5 2h9v6.5h-9zM1.3 2.6L5 5.6l3.7-3L5 6.6z"/></svg>
        hallo@wolkenbachtal.ch
      </li>
      <li>
        <svg viewBox="0 0 10 10"><circle cx="5" cy="5" r="4.5"/><path d="M3 2.5c1 .5 1.5 1.2 1 2s-1.5.5-1.5 1.5S4 7.5 4 8.5M6.5 1.5c-.5 1 0 1.5 1 2s1 1.5.5 2.5" fill="none" stroke="#f5f5f5" stroke-width=".8"/></svg>
        www.wolkenbachtal.ch
      </li>
    </ul>

    <div class="letter-body">
      <p class="salutation">Dear customer,</p>
      <p>Lorem ipsum dolor sit amet, consectetur adipisicing elit, sed do eiusmod tempor incididunt ut labore et dolore magna aliqua. Ut enim ad minim veniam, quis nostrud exercitation ullamco laboris nisi ut aliquip ex ea commodo consequat. Duis aute irure dolor in reprehenderit in voluptate velit esse cillum dolore eu fugiat nulla pariatur. Excepteur sint occaecat cupidatat non proident, sunt in culpa qui officia deserunt mollit anim id est laborum.</p>
      <p>Lorem ipsum dolor sit amet, consectetur adipisicing elit, sed do eiusmod tempor incididunt ut labore et dolore magna aliqua. Ut enim ad minim veniam, quis nostrud exercitation ullamco laboris nisi ut aliquip ex ea commodo consequat. Duis aute irure dolor in reprehenderit in voluptate velit esse cillum dolore eu fugiat nulla pariatur. Excepteur sint occaecat cupidatat non proident, sunt in culpa qui officia deserunt mollit anim id est laborum.</p>
      <p>Lorem ipsum dolor sit amet, consectetur adipisicing elit, sed do eiusmod tempor incididunt ut labore et dolore magna aliqua. Ut enim ad minim veniam, quis nostrud exercitation ullamco laboris nisi ut aliquip ex ea commodo consequat. Duis aute irure dolor in reprehenderit in voluptate velit esse cillum dolore eu fugiat nulla pariatur. Excepteur sint occaecat cupidatat non proident, sunt in culpa qui officia deserunt mollit anim id est laborum.</p>
      <p>Lorem ipsum dolor sit amet, consectetur adipisicing elit, sed do eiusmod tempor incididunt ut labore et dolore magna aliqua. Ut enim ad minim veniam, quis nostrud exercitation ullamco laboris nisi ut aliquip ex ea commodo consequat. Duis aute irure dolor in reprehenderit.</p>
      <p class="closing">Yours Sincerely,</p>
      <div class="signature-area" role="img" aria-label="Handwritten signature"></div>
    </div>

    <svg class="footer-band" viewBox="0 0 535 8" preserveAspectRatio="none" aria-hidden="true">
      <polygon points="0,0 264,0 270,8 0,8" fill="var(--ink)"/>
      <polygon points="267,0 535,0 535,8 273,8" fill="var(--rose)"/>
    </svg>
  </section>

</body>
</html>
```